依頼詳細
PCとスマホデザインの両方納品をいただきますが、
まずはデザインイメージが確認しやすいPCページのみの提案をお願いします。
スマホページは当選者に納品時にお願いしたいと思います。
スマホサイズは横幅750pxのサイズで作成してください。

レスポンシブウェブデザインを意識したデザインでお願いします。

デザインに関しては、添付してあるデザインレイアウト設計シートを基にお願いします。
参考サイトのURLはデザインレイアウト設計シートに記載してあります。

画像データについては、既存サイトや参考サイト、フリー素材から流用してイメージ画像に当て込んでください。
足りない場合は、一旦他のサイトの写真をサンプルとして入れてください。(サンプルなどの表記をお願いします)
ページ数
1ページ
希望イメージ
シンプル 複雑
単色 カラフル
暗い 明るい
日常 高級
遊び心 厳粛
未来的 伝統的
女性的 男性的
希望する色
青系、水色系、明るい色味
納品ファイル
• 高解像度JPG (.jpg)
• イラストレーター形式 (.ai)
• フォトショップ形式 (.psd)
• PNG形式 (.png)
補足説明
上記のいずれか1つ。アウトラインありとなしの2つ。

クライアントのイメージ通りでした。

たくさんのご提案ありがとうございました。
次回もぜひ、よろしくお願い致します。

```html
<!DOCTYPE html>
<html lang="ja">
<head>
<meta charset="UTF-8">
<title>ソラミ・プロダクツ株式会社</title>
<link href="https://fonts.googleapis.com/css2?family=Noto+Sans+JP:wght@400;500;700&family=Noto+Serif+JP:wght@500;700&display=swap" rel="stylesheet">
<style>
:root{
  --cyan:#2bbde0;
  --cyan-dark:#1aa6cb;
  --ink:#333;
  --muted:#777;
  --line:#ddd;
  --gray-bg:#eeeeee;
  --white:#fff;
  --red:#e53935;
  --wood:#b48a62;
  --wood-dark:#8a6646;
  --leaf:#7fae5a;
  --wall:#f3f1ed;
}
*{box-sizing:border-box;margin:0;padding:0}
html,body{width:1200px;height:2832px;overflow:hidden}
body{font-family:"Noto Sans JP",sans-serif;color:var(--ink);background:var(--white);position:relative}
a{text-decoration:none;color:inherit}
.serif{font-family:"Noto Serif JP",serif}

/* header */
.site-header{position:absolute;top:0;left:0;width:1200px;height:88px;background:var(--white)}
.brand{position:absolute;left:120px;top:18px;display:flex;align-items:center;gap:10px}
.brand-mark{width:22px;height:22px;border-radius:50%;background:var(--cyan)}
.brand-name{font-size:19px;font-weight:700;color:var(--ink)}
.global-nav{position:absolute;left:360px;top:62px;display:flex;gap:26px;font-size:12px;color:var(--ink)}
.search{position:absolute;left:622px;top:26px;width:190px;height:26px;border:1px solid var(--line);font-size:11px;color:#aaa;padding:5px 8px}
.search-btn{position:absolute;left:812px;top:26px;width:40px;height:26px;background:var(--cyan)}
.lang{position:absolute;left:880px;top:28px;display:flex;gap:8px}
.lang span{display:block;width:40px;height:22px;background:var(--cyan);border-radius:2px}
.contact-tab{position:absolute;right:0;top:0;width:150px;height:88px;background:var(--cyan);color:var(--white);text-align:center;font-size:12px;padding-top:22px}
.contact-tab svg{display:block;margin:0 auto 8px}

/* hero */
.hero{position:absolute;top:88px;left:0;width:1200px;height:652px;overflow:hidden;
  background:
    radial-gradient(ellipse 380px 300px at 860px 260px,rgba(255,255,255,.95),rgba(255,255,255,0) 70%),
    radial-gradient(ellipse 160px 200px at 1110px 190px,rgba(127,174,90,.55),rgba(127,174,90,0) 70%),
    radial-gradient(ellipse 140px 110px at 90px 190px,rgba(127,174,90,.45),rgba(127,174,90,0) 70%),
    radial-gradient(ellipse 200px 90px at 520px 560px,rgba(226,96,70,.35),rgba(226,96,70,0) 70%),
    linear-gradient(180deg,var(--wall) 0%,#e9e4dc 58%,var(--wood) 72%,var(--wood-dark) 100%)}
.hero-copy{position:absolute;left:150px;top:190px;font-size:30px;line-height:1.75;color:var(--ink);font-weight:700}
.hero-copy span{background:rgba(255,255,255,.85);padding:2px 10px}
.hero-btn{position:absolute;left:150px;top:300px;width:310px;height:66px;background:var(--cyan);color:var(--white);font-size:18px;font-weight:700;display:flex;align-items:center;padding-left:28px}
.arrow-tail{position:absolute;right:-40px;top:32px;width:80px;height:2px;background:var(--white)}
.arrow-tail::after{content:"";position:absolute;right:0;top:-6px;width:12px;height:2px;background:var(--white);transform:rotate(40deg);transform-origin:right}

/* section title */
.section-title{position:absolute;left:0;width:1200px;text-align:center;font-size:28px;font-weight:700}
.section-title::after{content:"";display:block;width:40px;height:2px;background:var(--cyan);margin:14px auto 0}

.center-btn{position:absolute;left:480px;width:240px;height:56px;background:var(--cyan);color:var(--white);font-size:15px;font-weight:500;display:flex;align-items:center;padding-left:40px}
.center-btn .arrow-tail{right:-30px;top:27px;width:70px}

/* products */
.carousel-arrow{position:absolute;top:1008px;z-index:2}
.product{position:absolute;top:940px;width:200px}
.product-photo{width:200px;height:180px;background:linear-gradient(160deg,#f2f2f2,#d9dde0)}
.product-tag{margin:10px auto 0;width:110px;height:20px;background:var(--cyan);color:var(--white);font-size:11px;text-align:center;line-height:20px}
.product-name{margin-top:10px;font-size:12px;text-align:center;color:var(--ink)}
.new-badge{position:absolute;left:-10px;top:-12px;width:36px;height:36px;border-radius:50%;background:var(--red)}
.dots{position:absolute;top:1252px;left:0;width:1200px;display:flex;justify-content:center;gap:8px}
.dots span{width:8px;height:8px;border-radius:50%;background:#ccc}
.dots span.on{background:var(--cyan)}

/* news */
.news-list{position:absolute;left:230px;top:1556px;width:740px;list-style:none}
.news-item{display:flex;align-items:center;height:36px;font-size:12px}
.news-date{width:100px;color:var(--ink)}
.news-cat{width:80px;height:20px;background:var(--cyan);color:var(--white);text-align:center;line-height:20px;font-size:11px;margin-right:20px}
.news-text{color:var(--cyan);text-decoration:underline}

/* features */
.feature{position:absolute;top:1856px;width:250px}
.feature-photo{width:250px;height:200px}
.feature-title{margin-top:26px;text-align:center;font-size:15px;font-weight:700}
.feature-text{margin-top:8px;font-size:11px;color:var(--muted);text-align:center;line-height:1.6}
.feature-btn{margin-top:14px;width:250px;height:48px;background:var(--cyan);color:var(--white);font-size:14px;display:flex;align-items:center;padding-left:60px;position:relative}
.feature-btn .arrow-tail{right:50px;top:23px;width:50px}

/* bottom band */
.info-band{position:absolute;top:2350px;left:0;width:1200px;height:330px;background:var(--gray-bg)}
.info-news{position:absolute;left:120px;top:54px;width:200px}
.info-news h2{font-size:26px;font-weight:700}
.info-news p{margin-top:16px;font-size:11px;line-height:1.7;color:var(--muted)}
.faq-box{position:absolute;left:462px;top:50px;width:276px;height:216px;background:var(--white);border:3px solid var(--cyan);display:flex;flex-direction:column;align-items:center;justify-content:center;gap:14px;font-size:16px;font-weight:700}
.contact-box{position:absolute;left:790px;top:50px;width:260px;height:216px;background:var(--white);border:3px solid var(--cyan);text-align:center;padding-top:36px}
.contact-box .label{font-size:13px;font-weight:700}
.contact-box .tel{margin-top:8px;font-size:26px;font-weight:700;color:var(--cyan-dark);display:flex;align-items:center;justify-content:center;gap:8px}
.contact-box .mail{margin:18px auto 0;width:200px;height:34px;background:var(--cyan);color:var(--white);font-size:12px;line-height:34px}

/* footer */
.site-footer{position:absolute;top:2680px;left:0;width:1200px;height:152px;background:var(--cyan);color:var(--white)}
.footer-links{position:absolute;left:120px;top:28px;display:flex;gap:60px;font-size:11px;line-height:1.9}
.footer-links ul{list-style:none}
.footer-brand{position:absolute;left:500px;top:30px;display:flex;align-items:center;gap:10px}
.footer-brand .brand-mark{background:var(--white)}
.footer-brand .brand-name{color:var(--white);font-size:18px}
.footer-address{position:absolute;left:500px;top:66px;font-size:11px;line-height:1.8}
.pagetop{position:absolute;right:60px;top:-56px;width:56px;height:56px;background:var(--cyan);display:flex;align-items:center;justify-content:center}
</style>
</head>
<body>

<header class="site-header">
  <div class="brand"><span class="brand-mark"></span><span class="brand-name">ソラミ・プロダクツ株式会社</span></div>
  <nav class="global-nav"><span>ソラミ・プロダクツとは</span><span>商品一覧</span><span>新商品</span><span>WEBカタログ</span><span>直営ショップ</span><span>会社案内</span></nav>
  <div class="search">Search</div><div class="search-btn"></div>
  <div class="lang"><span></span><span></span></div>
  <a class="contact-tab">
    <svg width="22" height="16" viewBox="0 0 22 16"><rect x="1" y="1" width="20" height="14" fill="none" stroke="#fff" stroke-width="2"/><path d="M1 1 L11 9 L21 1" fill="none" stroke="#fff" stroke-width="2"/></svg>
    お問い合わせ
  </a>
</header>

<section class="hero" role="img" aria-label="明るいキッチンで野菜を調理する女性の写真">
  <p class="hero-copy serif"><span>ソラミ・プロダクツの商品が</span><br><span>日々の生活に新提案</span></p>
  <a class="hero-btn">ソラミ・プロダクツとは<span class="arrow-tail"></span></a>
</section>

<h2 class="section-title serif" style="top:790px">商品紹介</h2>

<svg class="carousel-arrow" style="left:136px" width="26" height="44" viewBox="0 0 26 44"><path d="M22 4 L4 22 L22 40" fill="none" stroke="#444" stroke-width="5"/></svg>
<svg class="carousel-arrow" style="left:1040px" width="26" height="44" viewBox="0 0 26 44"><path d="M4 4 L22 22 L4 40" fill="none" stroke="#444" stroke-width="5"/></svg>

<div class="product" style="left:190px"><div class="product-photo" role="img" aria-label="キッチン用品の商品写真"></div><span class="new-badge"></span><div class="product-tag">キッチン用品</div><p class="product-name">手に優しい野菜ピーラー</p></div>
<div class="product" style="left:400px"><div class="product-photo" role="img" aria-label="キッチン用品の商品写真"></div><div class="product-tag">キッチン用品</div><p class="product-name">コンパクト卓上研ぎ器</p></div>
<div class="product" style="left:610px"><div class="product-photo" role="img" aria-label="収納用品の商品写真"></div><div class="product-tag">収納用品</div><p class="product-name">スリムワゴン 5段タイプ</p></div>
<div class="product" style="left:820px"><div class="product-photo" role="img" aria-label="生活雑貨の商品写真"></div><div class="product-tag">生活雑貨</div><p class="product-name">詰め替え用ボトル 3本組</p></div>

<div class="dots"><span class="on"></span><span></span><span></span></div>
<a class="center-btn" style="top:1300px">商品一覧はこちら<span class="arrow-tail"></span></a>

<h2 class="section-title serif" style="top:1460px">お知らせ</h2>
<ul class="news-list">
  <li class="news-item"><span class="news-date">2020年07月01日</span><span class="news-cat">新商品</span><span class="news-text">夏向けの新しいキッチン用品を発売しました。詳細は商品ページをご覧ください。</span></li>
  <li class="news-item"><span class="news-date">2020年06月15日</span><span class="news-cat">お知らせ</span><span class="news-text">夏季休業期間のお知らせを掲載しました。ご確認をお願いいたします。</span></li>
  <li class="news-item"><span class="news-date">2020年06月01日</span><span class="news-cat">お知らせ</span><span class="news-text">WEBカタログを更新しました。最新の商品情報をご覧いただけます。</span></li>
</ul>
<a class="center-btn" style="top:1722px">一覧はこちら<span class="arrow-tail"></span></a>

<div class="feature" style="left:150px">
  <div class="feature-photo" role="img" aria-label="会社の社屋外観の写真" style="background:linear-gradient(180deg,#c9dbe8 0%,#c9dbe8 35%,#9aa1a6 36%,#7d8488 100%)"></div>
  <h3 class="feature-title">会社案内</h3>
  <p class="feature-text">私たちの歩みと事業内容、<br>会社概要をご紹介します。</p>
  <a class="feature-btn">詳細はこちら<span class="arrow-tail"></span></a>
</div>
<div class="feature" style="left:475px">
  <div class="feature-photo" role="img" aria-label="カタログ誌面の画像" style="background:linear-gradient(135deg,#f4f6f8,#dfe6ec)"></div>
  <h3 class="feature-title">WEBカタログ</h3>
  <p class="feature-text">最新の商品カタログを<br>オンラインでご覧いただけます。</p>
  <a class="feature-btn">詳細はこちら<span class="arrow-tail"></span></a>
</div>
<div class="feature" style="left:800px">
  <div class="feature-photo" style="background:var(--white);border:1px solid var(--line);display:flex;align-items:center;justify-content:center;font-size:24px;font-weight:700">コモレビショップ</div>
  <h3 class="feature-title">直営ショップ</h3>
  <p class="feature-text">公式オンラインショップで<br>商品をお買い求めいただけます。</p>
  <a class="feature-btn">詳細はこちら<span class="arrow-tail"></span></a>
</div>

<section class="info-band">
  <div class="info-news"><h2 class="serif">お知らせ</h2><p>ソラミ・プロダクツからの<br>お知らせをご覧ください。</p></div>
  <a class="faq-box">
    <svg width="40" height="40" viewBox="0 0 40 40"><circle cx="20" cy="20" r="17" fill="none" stroke="#2bbde0" stroke-width="3"/><text x="20" y="27" text-anchor="middle" font-size="20" font-weight="700" fill="#2bbde0" font-family="Noto Sans JP,sans-serif">?</text></svg>
    よくあるご質問
  </a>
  <div class="contact-box">
    <p class="label">お問い合わせ</p>
    <p class="tel"><svg width="22" height="22" viewBox="0 0 24 24"><path d="M6.6 10.8a15 15 0 0 0 6.6 6.6l2.2-2.2c.3-.3.7-.4 1-.2 1.1.4 2.3.6 3.6.6.6 0 1 .4 1 1V20c0 .6-.4 1-1 1A17 17 0 0 1 3 4c0-.6.4-1 1-1h3.5c.6 0 1 .4 1 1 0 1.3.2 2.5.6 3.6.1.3 0 .7-.2 1z" fill="#1aa6cb"/></svg>0256-00-1234</p>
    <p style="font-size:11px;color:#777;margin-top:4px">受付時間 平日9:00〜17:00</p>
    <p class="mail">メールでお問い合わせ</p>
  </div>
</section>

<footer class="site-footer">
  <a class="pagetop"><svg width="24" height="24" viewBox="0 0 24 24"><path d="M4 14 L12 6 L20 14 M12 6 V22" fill="none" stroke="#fff" stroke-width="3"/></svg></a>
  <div class="footer-links">
    <ul><li>HOME</li><li>ソラミ・プロダクツとは</li><li>商品一覧</li><li>新商品</li><li>お知らせ</li></ul>
    <ul><li>WEBカタログ</li><li>直営ショップ</li><li>会社案内</li><li>よくあるご質問</li><li>お問い合わせ</li></ul>
  </div>
  <div class="footer-brand"><span class="brand-mark"></span><span class="brand-name">ソラミ・プロダクツ株式会社</span></div>
  <p class="footer-address">〒000-0000 新潟県見本市中央町1-2-3<br>TEL 0256-00-1234 / FAX 0256-00-1235</p>
</footer>

</body>
</html>
```